Frost Leaf: CBD and Herbal Topical Pain product needs a brochure

We need a brochure that educates customers on the product. The product combines traditional Chinese herbs used for pain and swelling with a strong dose of CBD to apply topical with a glass, roll-on applicator. We would like to see dark blue as a dominant color or anything ice related. The logo is an iceberg but doesn't need to be included.

Target Market(s)

Cannabis Dispensaries, Chiro, Acu offices,
Health / Wellness, Alternative Medicine

Industry/Entity Type

Alternative Medicine

Colors
0455a3

Requirements
Must have
• Frost Leaf
• 500mg CBD in 1oz
• For: Muscle, Joint Pain, Swelling, Acute Injuries, Chronic Pain, Arthritis
• Directions: Apply a thin layer of herbal formula over the affected area. Apply as needed.
• Caution: Avoid hot water shortly after application.
• Ingredients: Angelica Root, Camphor, Cannabidoil (CBD), Cinnamon, Dandelion, Gardenia, Ginger, Licorice, Menthol, Myrrh, Phellodendron Bark, Rhubarb, Safflower, Sesame Oil, Scutellaria
• Highlight amount of CBD: 500mg
• Secondary highlights it includes Turmeric and Magnesium
• Easy Roll-On Topical Pain Relief for Muscle Spasms, Joint Pain, Strains, Sprains, Swelling
• Increases circulation to increase recovery time. Great for athletes
• Stops pain by numbing painful, slower deep nerve signals by stimulating the faster, superficial nerves with a cooling sensation
• Reduce painful swelling and heat involved with inflammation.
• Breaks up damaged tissue to enhance the natural healing process
• Ingredients
• Dang Gui – Angelica : reduces swelling, generates tissue, alleviates pain, expels pus
• Cinnamon –Gui Zhi decreases arthritic pain
• Carthamus Flower / safflower –Hong Hua - reduces swelling, alleviates pain,
• Rhubarb – Da Huang -bruising, acute and chronic swelling
• Licorice –Gan Cao - alleviates spasms, anti-inflammatory
• Phellodendron Huang Bai– reduces swelling and pain
• Dandelion – Pu Gong Ying – reduces swelling and nodules, anti-inflammatory
• Mo Yao – Myrrh – reduces swelling, pain, bruising, and masses, promotes healing
• Ginger – Gan Jiang – chronic swelling, increases circulation
• Gardenia – Zhi Zi- Reduces swelling from trauma, bruising
• Scutellaria – Huang Qin – hot sores, swelling,
• Magnesium – helps muscle spasms
• Camphor – mild, local anesthetic effect, alleviates pain, pain and swelling from sprains
• Menthol – rashes, swelling, relaxes muscles
• Turmeric – reduces inflammation and swelling
• Sesame Oil – carrier oil
• Cannabidiol (CBD) Isolate
• Colloidal Silver (Natural Preservative)
• Formulated by a Herbalist and Doctor of Chinese Medicine, Dr. Wendell Prasky, DAOM
Nice to have
• Iceberg or ice theme
• Copy:
• Frost Leaf blends traditional Chinese herbs with a potent dose of hemp derived cannabidiol (CBD) isolate. Instantly feel the cooling icy sensation penetrate deep into sore muscles and joints to sooth away pain.
• Not only does the menthol give a temporary cooling effect which helps numb pain, the other herbal ingredients continue to soothe tight, achy muscles and joints. It can also be applied for an acute sprain or strain to reduce swelling, just like applying ice.
• Ice is used by athletes and recommended by doctors to reduce pain and swelling. Frost Leaf can reduce pain and swelling without having to carry a bag of ice around.
• With the easy roll-on application, you dont even have to get your hands cold!
• Traditional Chinese Medicine has used the same herbs for thousands of years to help ease the pain of injuries during battle. Herbal plasters, liniments, and oils were the most common application to maximize the healing benefits of the herbs. Frost Leaf uses organic, raw herbs which are ground into a fine powder and further extracted in sesame oil. Once extracted, the oil is filtered and then CBD is then added as the oil is cooling.
• Pictures of a few of the herbs - I have a few already if needed

```html
<!DOCTYPE html>
<html lang="en">
<head>
<meta charset="utf-8">
<title>Frost Leaf – Tri-fold Brochure</title>
<link href="https://fonts.googleapis.com/css2?family=Lato:ital,wght@0,400;0,700;0,900;1,400&display=swap" rel="stylesheet">
<style>
  :root{
    --brand-blue:#0455a3;
    --navy:#2b2642;
    --ink:#2a2a35;
    --body-grey:#55585f;
    --paper:#ffffff;
    --backdrop:#e3e4e7;
  }
  *{box-sizing:border-box;margin:0;padding:0}
  html,body{width:1200px;height:1200px;overflow:hidden;background:var(--backdrop)}
  body{font-family:"Lato",sans-serif;color:var(--ink)}
  .canvas{position:relative;width:1200px;height:1200px}
  .spread{position:absolute;left:40px;width:1120px;height:550px;background:var(--paper);box-shadow:0 6px 22px rgba(0,0,0,.18)}
  .spread--inside{top:35px}
  .spread--outside{top:615px}
  .spread__shapes{position:absolute;inset:0;width:1120px;height:550px}
  .block{position:absolute}
  ul.list{list-style:none}
  ul.list li{position:relative;padding-left:14px}
  ul.list li::before{content:"";position:absolute;left:0;top:.45em;width:6px;height:6px;border-radius:50%;background:var(--brand-blue)}

  /* inside panel 1 */
  .product-intro{left:28px;top:26px;width:320px}
  .product-intro__title{font-weight:900;font-size:36px;color:var(--brand-blue);line-height:1}
  .product-intro__dose{font-weight:700;font-size:16px;margin:10px 0 10px}
  .product-intro .list li{font-size:11px;line-height:1.35;color:var(--body-grey);margin-bottom:9px}

  /* inside panel 2 */
  .highlights{left:392px;top:318px;width:340px;color:#fff}
  .highlights__title{font-weight:700;font-size:19px;margin-bottom:8px}
  .highlights .list li{font-size:10.5px;line-height:1.32;margin-bottom:6px}
  .highlights .list li::before{background:#fff}

  /* inside panel 3 */
  .ingredients{left:800px;top:26px;width:300px}
  .ingredients .list li{font-size:9.8px;line-height:1.28;color:var(--body-grey);margin-bottom:3px}
  .ingredients b{color:var(--ink)}

  /* outside panel 1 */
  .story{left:26px;top:34px;width:320px}
  .story .list li{font-size:10.5px;line-height:1.33;font-style:italic;color:var(--body-grey);margin-bottom:8px}
  .story .list li:first-child{padding-right:40px}

  /* outside panel 2 */
  .contact{left:400px;top:300px;width:300px;text-align:center;color:#fff;font-size:13px;line-height:1.45}
  .back-brand{left:440px;top:420px;width:220px;text-align:center;color:#fff}
  .back-brand__name{font-weight:700;font-size:15px}
  .back-brand__line{font-size:11px;margin-top:14px}
  .back-brand__small{font-size:7px;margin-top:2px}

  /* outside panel 3 */
  .cover-brand{left:843px;top:338px;width:180px;height:180px;background:var(--navy);color:#fff;text-align:center;padding-top:34px}
  .cover-brand__name{font-weight:700;font-size:26px}
  .cover-brand__mark{width:14px;height:14px;border-radius:50%;background:#fff;margin:16px auto 14px}
  .cover-brand__line{font-size:14px;font-weight:700}
  .cover-brand__small{font-size:9px;margin-top:4px}
</style>
</head>
<body>
<main class="canvas">

  <!-- Inside spread -->
  <section class="spread spread--inside">
    <svg class="spread__shapes" viewBox="0 0 1120 550" xmlns="http://www.w3.org/2000/svg">
      <defs>
        <linearGradient id="citrusDrink" x1="0" y1="0" x2="1" y2="1">
          <stop offset="0" stop-color="#f1eee8"/><stop offset=".55" stop-color="#f2b35a"/><stop offset="1" stop-color="#e8dccb"/>
        </linearGradient>
        <linearGradient id="berryDrink" x1="0" y1="0" x2="1" y2="1">
          <stop offset="0" stop-color="#e9efe3"/><stop offset=".45" stop-color="#c8384a"/><stop offset=".8" stop-color="#8a2a3a"/><stop offset="1" stop-color="#dfe7da"/>
        </linearGradient>
      </defs>
      <g role="img" aria-label="Photo of iced herbal citrus drinks with berries and ginger">
        <rect x="0" y="280" width="373" height="270" fill="url(#citrusDrink)"/>
      </g>
      <g role="img" aria-label="Photo of iced red herbal drinks with fresh herbs and flowers">
        <rect x="373" y="0" width="374" height="330" fill="url(#berryDrink)"/>
      </g>
      <path d="M373,305 Q560,285 747,235 C760,370 770,470 785,550 L373,550 Z" fill="var(--brand-blue)"/>
      <path d="M747,0 L1120,0 L1120,10 Q920,14 747,40 Z" fill="var(--brand-blue)"/>
    </svg>

    <div class="block product-intro">
      <h1 class="product-intro__title">Frost Leaf</h1>
      <p class="product-intro__dose">500mg CBD in 1oz</p>
      <ul class="list">
        <li>For: Muscle, Joint Pain, Swelling, Acute Injuries, Chronic Pain, Arthritis</li>
        <li>Directions: Apply a thin layer of herbal formula over the affected area. Apply as needed.</li>
        <li>Caution: Avoid hot water shortly after application.</li>
        <li>Ingredients: Angelica Root, Camphor, Cannabidoil (CBD), Cinnamon, Dandelion, Gardenia, Ginger, Licorice, Menthol, Myrrh, Phellodendron Bark, Rhubarb, Safflower, Sesame Oil, Scutellaria</li>
      </ul>
    </div>

    <div class="block highlights">
      <h2 class="highlights__title">Highlight amount of CBD: 500mg</h2>
      <ul class="list">
        <li>Secondary highlights it includes Turmeric and Magnesium</li>
        <li>Easy Roll-On Topical Pain Relief for Muscle Spasms, Joint Pain, Strains, Sprains, Swelling</li>
        <li>Increases circulation to increase recovery time. Great for athletes</li>
        <li>Stops pain by numbing painful, slower deep nerve signals by stimulating the faster, superficial nerves with a cooling sensation</li>
        <li>Reduce painful swelling and heat involved with inflammation.</li>
        <li>Breaks up damaged tissue to enhance the natural healing process</li>
        <li>Ingredients</li>
      </ul>
    </div>

    <div class="block ingredients">
      <ul class="list">
        <li><b>Dang Gui</b> – Angelica : reduces swelling, generates tissue, alleviates pain, expels pus</li>
        <li><b>Cinnamon</b> –Gui Zhi decreases arthritic pain</li>
        <li><b>Carthamus Flower / safflower</b> –Hong Hua - reduces swelling, alleviates pain,</li>
        <li><b>Rhubarb</b> – Da Huang -bruising, acute and chronic swelling</li>
        <li><b>Licorice</b> –Gan Cao - alleviates spasms, anti-inflammatory</li>
        <li><b>Phellodendron Huang Bai</b>– reduces swelling and pain</li>
        <li><b>Dandelion</b> – Pu Gong Ying – reduces swelling and nodules, anti-inflammatory</li>
        <li><b>Mo Yao</b> – Myrrh – reduces swelling, pain, bruising, and masses, promotes healing</li>
        <li><b>Ginger</b> – Gan Jiang – chronic swelling, increases circulation</li>
        <li><b>Gardenia</b> – Zhi Zi- Reduces swelling from trauma, bruising</li>
        <li><b>Scutellaria</b> – Huang Qin – hot sores, swelling,</li>
        <li><b>Magnesium</b> – helps muscle spasms</li>
        <li><b>Camphor</b> – mild, local anesthetic effect, alleviates pain, pain and swelling from sprains</li>
        <li><b>Menthol</b> – rashes, swelling, relaxes muscles</li>
        <li><b>Turmeric</b> – reduces inflammation and swelling</li>
        <li><b>Sesame Oil</b> – carrier oil</li>
        <li>Cannabidiol (CBD) Isolate</li>
        <li>Colloidal Silver (Natural Preservative)</li>
        <li>Formulated by a Herbalist and Doctor of Chinese Medicine, Dr. Wendell Prasky, DAOM</li>
      </ul>
    </div>
  </section>

  <!-- Outside spread -->
  <section class="spread spread--outside">
    <svg class="spread__shapes" viewBox="0 0 1120 550" xmlns="http://www.w3.org/2000/svg">
      <defs>
        <linearGradient id="mortarHerbs" x1="0" y1="0" x2="1" y2="1">
          <stop offset="0" stop-color="#b07a3e"/><stop offset=".35" stop-color="#5e8a3c"/><stop offset=".6" stop-color="#cfcac0"/><stop offset="1" stop-color="#d89a55"/>
        </linearGradient>
      </defs>
      <g role="img" aria-label="Photo of a stone mortar and pestle filled with fresh green herbs and small purple flowers">
        <rect x="460" y="0" width="660" height="400" fill="url(#mortarHerbs)"/>
      </g>
      <path d="M373,0 L470,0 C520,50 500,100 373,125 Z" fill="var(--paper)"/>
      <path d="M470,0 C520,50 500,100 373,125" fill="none" stroke="var(--brand-blue)" stroke-width="8"/>
      <path d="M373,120 C470,110 560,140 620,200 C690,270 725,340 740,400 L747,550 L373,550 Z" fill="var(--navy)"/>
      <path d="M373,120 C470,110 560,140 620,200 C690,270 725,340 740,400" fill="none" stroke="var(--brand-blue)" stroke-width="4"/>
      <rect x="747" y="400" width="373" height="150" fill="var(--paper)"/>
      <path d="M0,530 Q190,515 373,522 L373,550 L0,550 Z" fill="var(--brand-blue)"/>
      <path d="M747,522 Q930,515 1120,530 L1120,550 L747,550 Z" fill="var(--brand-blue)"/>
    </svg>

    <div class="block story">
      <ul class="list">
        <li>Frost Leaf blends traditional Chinese herbs with a potent dose of hemp derived cannabidiol (CBD) isolate. Instantly feel the cooling icy sensation penetrate deep into sore muscles and joints to sooth away pain.</li>
        <li>Not only does the menthol give a temporary cooling effect which helps numb pain, the other herbal ingredients continue to soothe tight, achy muscles and joints. It can also be applied for an acute sprain or strain to reduce swelling, just like applying ice.</li>
        <li>Ice is used by athletes and recommended by doctors to reduce pain and swelling. Frost Leaf can reduce pain and swelling without having to carry a bag of ice around.</li>
        <li>With the easy roll-on application, you dont even have to get your hands cold!</li>
        <li>Traditional Chinese Medicine has used the same herbs for thousands of years to help ease the pain of injuries during battle. Herbal plasters, liniments, and oils were the most common application to maximize the healing benefits of the herbs. Frost Leaf uses organic, raw herbs which are ground into a fine powder.</li>
      </ul>
    </div>

    <address class="block contact" style="font-style:normal">
      Adress: 12 Glacier Row, Northbrook<br>
      Phone: 0000 00 00<br>
      Email: hello@frostleaf-care.com<br>
      www.frostleaf-care.com
    </address>

    <div class="block back-brand">
      <p class="back-brand__name">Frost Leaf</p>
      <p class="back-brand__line">Pain Relief</p>
      <p class="back-brand__small">Menthol, CBD, Turmeric &amp; Magnesium</p>
      <p class="back-brand__small">1 fl oz</p>
    </div>

    <div class="block cover-brand">
      <p class="cover-brand__name">Frost Leaf</p>
      <div class="cover-brand__mark"></div>
      <p class="cover-brand__line">Pain Relief</p>
      <p class="cover-brand__small">Menthol, CBD, Turmeric &amp; Magnesium</p>
      <p class="cover-brand__small">1 fl oz</p>
    </div>
  </section>

</main>
</body>
</html>
```